Industrial Supply Marketing Handout

Looking for a 5"x7" card sized marketing piece that we will hand out to prospects on cold calls and also be able to mail as a post card. Needs to highlight the types of products we sell and refer them to my new website. There should also be a prominent spot that a discount code can be written in with that something to the effect that they are free to share that discount code with anyone. My website address is www.brenkato.com for reference to the site's look and product line. The site also has an "Industry Guide" in the links that brings up suggested items for different types of businesses. Overall the products being pushed are janitorial and safety products. Zipped file is uploaded with a variety of logo formats. Targeted buisnesses are: Industrial facilities, auto repair, body shops, aircraft repair facilities, FBO's, schools, and building service contractors (contract building cleaning companies), medical offices, gyms, residential and comercial property management companies, and construction companies.

Target Market(s)

Industrial facilities, manufacturing, auto repair, body shops, aircraft repair facilities, FBO's, schools, and building service contractors (contract building cleaning companies), medical offices, gyms, residential and comercial property management companies, and construction companies

Industry/Entity Type

Marketing

Requirements
Must have
• Logo, website address prominently displayed, discount code field
Nice to have
• Industrial grunge feel

```html
<!DOCTYPE html>
<html lang="en">
<head>
<meta charset="utf-8">
<title>Brenkato Supply – Marketing Card</title>
<link href="https://fonts.googleapis.com/css2?family=Open+Sans:ital,wght@0,400;0,600;0,700;1,400&display=swap" rel="stylesheet">
<style>
  :root {
    --paper: #f4f5f6;
    --band: #0b8fd0;
    --band-deep: #0579b8;
    --cyan: #14b4ec;
    --cyan-light: #6fd3f5;
    --white: #ffffff;
    --navy: #0e3f73;
    --link: #1a7fc0;
    --grey: #8a8c8e;
    --logo: #1d5fa8;
  }
  html, body {
    margin: 0;
    padding: 0;
    overflow: hidden;
  }
  body {
    width: 1200px;
    height: 856px;
    background: var(--paper);
    font-family: "Open Sans", Arial, sans-serif;
  }
  .card {
    position: relative;
    width: 1200px;
    height: 856px;
    overflow: hidden;
    background: var(--paper);
  }
  .card__waves {
    position: absolute;
    inset: 0;
  }
  .brand {
    position: absolute;
    left: 760px;
    top: 70px;
    display: flex;
    align-items: center;
    gap: 14px;
  }
  .brand__mark {
    width: 22px;
    height: 22px;
    border-radius: 50%;
    background: var(--logo);
  }
  .brand__name {
    font-size: 38px;
    font-weight: 700;
    color: var(--logo);
    letter-spacing: 0.5px;
  }
  .product-photo {
    position: absolute;
    left: 24px;
    top: 62px;
    width: 560px;
    height: 458px;
    border-radius: 46% 40% 34% 30% / 30% 34% 38% 40%;
    background: radial-gradient(ellipse at 45% 55%, #2f8de3 0%, #1d6fc9 55%, rgba(29, 111, 201, 0.0) 78%);
  }
  .discount {
    position: absolute;
    left: 40px;
    top: 528px;
    width: 520px;
    height: 66px;
    box-sizing: border-box;
    padding: 7px 18px;
    background: var(--white);
    border: 2px dashed var(--navy);
    border-radius: 8px;
    color: var(--navy);
  }
  .discount__row {
    display: flex;
    align-items: flex-end;
    gap: 12px;
    font-size: 19px;
    font-weight: 700;
    line-height: 26px;
  }
  .discount__blank {
    flex: 1;
    height: 20px;
    border-bottom: 2px solid var(--navy);
  }
  .discount__note {
    margin: 2px 0 0;
    font-size: 14px;
    font-style: italic;
    line-height: 20px;
    color: var(--band-deep);
  }
  .pitch {
    position: absolute;
    left: 623px;
    top: 241px;
    width: 452px;
    margin: 0;
    color: var(--white);
    font-size: 20.5px;
    line-height: 31px;
  }
  .range__title {
    position: absolute;
    left: 623px;
    top: 384px;
    margin: 0;
    padding-bottom: 4px;
    width: 360px;
    border-bottom: 2px solid var(--white);
    color: var(--white);
    font-size: 21px;
    font-weight: 700;
  }
  .range__list {
    position: absolute;
    left: 678px;
    top: 427px;
    margin: 0;
    padding: 0;
    list-style: none;
    display: grid;
    grid-template-columns: 273px 240px;
    row-gap: 20px;
    color: var(--white);
    font-size: 23px;
    line-height: 34px;
  }
  .range__list li {
    position: relative;
  }
  .range__list li:nth-child(n+5) {
    margin-top: -12px;
  }
  .range__list li::before {
    content: "";
    position: absolute;
    left: -20px;
    top: 13px;
    width: 10px;
    height: 10px;
    border-radius: 50%;
    background: var(--navy);
  }
  .range__note {
    position: absolute;
    left: 654px;
    top: 597px;
    margin: 0;
    color: var(--white);
    font-size: 20px;
    font-style: italic;
  }
  .contact {
    position: absolute;
    margin: 0;
    font-size: 28px;
    line-height: 38px;
  }
  .contact__label {
    display: block;
    color: var(--navy);
  }
  .contact__value {
    display: block;
    color: var(--grey);
  }
  .contact--phone { left: 22px; top: 726px; }
  .contact--web { left: 435px; top: 764px; color: var(--link); }
  .contact--email { left: 858px; top: 720px; }
</style>
</head>
<body>
<main class="card">
  <svg class="card__waves" width="1200" height="856" viewBox="0 0 1200 856" aria-hidden="true">
    <path d="M0,190 C320,178 700,205 1200,140 L1200,640 C900,660 420,620 0,610 Z" fill="var(--band)"/>
    <path d="M0,190 C300,182 560,190 820,184 C560,200 260,204 0,214 Z" fill="var(--cyan)"/>
    <path d="M760,212 C900,196 1060,170 1200,150 L1200,178 C1060,196 900,210 760,212 Z" fill="var(--white)" opacity="0.9"/>
    <path d="M0,560 C360,600 760,640 1200,616 L1200,648 C760,672 360,640 0,600 Z" fill="var(--band-deep)"/>
    <path d="M0,600 C380,640 760,672 1200,648 L1200,664 C760,690 380,664 0,626 Z" fill="var(--white)"/>
    <path d="M40,640 C420,668 800,690 1200,664 L1200,678 C800,706 420,690 40,646 Z" fill="var(--cyan)"/>
    <path d="M200,676 C560,696 880,700 1200,686 L1200,692 C880,710 560,708 200,680 Z" fill="var(--cyan-light)"/>
  </svg>

  <div class="brand">
    <span class="brand__mark"></span>
    <span class="brand__name">Brenkato Supply</span>
  </div>

  <div class="product-photo" role="img" aria-label="Photo of a blue bucket filled with cleaning supplies: spray bottle, brushes, sponge, squeegee, detergent jug and yellow rubber gloves"></div>

  <section class="discount" aria-label="Discount code">
    <div class="discount__row">
      <span class="discount__label">Your Discount Code:</span>
      <span class="discount__blank"></span>
    </div>
    <p class="discount__note">Feel free to share this code with anyone!</p>
  </section>

  <p class="pitch">We have competitive shipping rates, no fuel surcharges, no minimums, and fast shipping. We offer our products to individuals at the same low wholesale pricing.</p>

  <h2 class="range__title">Our Wide Product Range:</h2>
  <ul class="range__list">
    <li>Janitorial</li>
    <li>Office Supplies</li>
    <li>Safety &amp; Security</li>
    <li>Maintenance &amp;<br>Breakroom</li>
    <li>Food Services</li>
    <li>Industry Guides</li>
  </ul>
  <p class="range__note">For details, visit our website....</p>

  <p class="contact contact--phone">
    <span class="contact__label">Call Us:</span>
    <span class="contact__value">000 000 0000</span>
  </p>
  <p class="contact contact--web">www.brenkato.com</p>
  <p class="contact contact--email">
    <span class="contact__label">Email Customer Service:</span>
    <span class="contact__value">info@brenkato.com</span>
  </p>
</main>
</body>
</html>
```